Wow, Spring Is Near!

I am a mobile weight loss consultant. I have partnered up with the Vitality Kickoff scheme which is based on real food. I travel to my clients at work or at home or in my own home office. My target audience is mothers -especial younger mothers with school kids and its time for my clients to focus on themselves they are worth it. I have over 10 years experience as a weight loss consultant. No contracts and no risk and i want them directed to my Facebook page BrightpathWellnessGuide or call me on 0439582706.

I am looking for a flyer to attached to his brochure early Feb for the mothers with all the kids going to back to school. ( i will attach so you can see it).
I have attached VK advertising with the girl and the banana. I do like the vk official partner somewhere on it?? I like the back drop as the girl with a banana or a mum and kids ?? I don't know

Limitied places so be quick

I have attached my logo as well.

Any questions plz ask I just need something when mothers see it, they will look twice and just chuck it in the bin??
Thank you
Maren

Just leaning how to use sketch hive so I have updated my information to help you. Thank you

Reason: I am getting many great designs. I am currently on holidays and get home tomorrow and would like a couple of days to get my friends options etc before I decide. Thank you to all designers

Target Market(s)

mothers, especially young mums with kids at school- which will just be starting back at school in February.

Industry/Entity Type

Advertising

Requirements
Must have
• somehow :-
- no contracts with no risk
- experienced
- i go to them at home or work
- real food
Should not have
• The word "diet"

```html
<!DOCTYPE html>
<html lang="en">
<head>
<meta charset="utf-8">
<title>Brightpath Wellness Guide – Flyer</title>
<link rel="stylesheet" href="https://fonts.googleapis.com/css2?family=Oswald:wght@500;600&family=Roboto+Condensed:wght@300;400&family=Lato:wght@700&display=swap">
<style>
  :root {
    --pink: #e8717b;
    --purple: #985a9e;
    --purple-text: #9a55a3;
    --yellow: #f8e3a1;
    --white: #ffffff;
    --grey-text: #555555;
    --page: #ecebe9;
    --photo-warm: #d8c0b2;
    --photo-light: #f3ece6;
    --produce-tone: #9cc7c9;
    --produce-soft: #d7e9e4;
  }
  * { margin: 0; padding: 0; box-sizing: border-box; }
  html, body { width: 1200px; height: 900px; overflow: hidden; }
  body { background: var(--page); position: relative; }

  .flyer {
    position: absolute; left: 50px; top: 185px;
    width: 1100px; height: 530px;
    background: var(--white); overflow: hidden;
  }
  .flyer__photo {
    position: absolute; left: 0; top: 60px; width: 560px; height: 430px;
    background: linear-gradient(90deg, var(--photo-warm) 0%, var(--photo-light) 70%, rgba(255,255,255,0) 100%);
  }
  .flyer__shapes { position: absolute; inset: 0; }
  .flyer__produce {
    position: absolute; left: 50px; top: 295px; width: 260px; height: 210px;
    border-radius: 24px;
    background: linear-gradient(160deg, var(--produce-soft) 0%, var(--produce-tone) 100%);
  }

  .offer { position: absolute; right: 28px; top: 20px; text-align: right; }
  .offer__headline {
    font-family: 'Oswald', sans-serif; font-weight: 600; font-size: 20px;
    color: var(--yellow); letter-spacing: 0.6px; line-height: 1.2;
  }
  .offer__experience {
    font-family: Arial, Helvetica, sans-serif; font-size: 14px;
    color: var(--white); margin-top: 5px; letter-spacing: 0.4px;
  }
  .offer__terms {
    font-family: 'Oswald', sans-serif; font-weight: 500; font-size: 14px;
    color: var(--yellow); line-height: 1.45; margin-top: 4px; letter-spacing: 0.3px;
  }

  .brand-badge {
    position: absolute; left: 598px; top: 116px; width: 356px; height: 148px;
    border: 6px solid var(--pink); border-radius: 50%; background: var(--white);
    display: flex; align-items: center; justify-content: center; text-align: center;
  }
  .brand-badge__name {
    font-family: 'Oswald', sans-serif; font-weight: 600; font-size: 30px;
    color: var(--purple-text); line-height: 1.1;
  }

  .message { position: absolute; left: 465px; top: 276px; white-space: nowrap; }
  .message__headline {
    font-family: 'Oswald', sans-serif; font-weight: 600; font-size: 39px;
    color: var(--purple-text); letter-spacing: 0.4px;
  }
  .message__question {
    font-family: 'Oswald', sans-serif; font-weight: 500; font-size: 27px;
    color: var(--pink); margin-left: 8px;
  }
  .message__sub {
    font-family: 'Roboto Condensed', sans-serif; font-weight: 300; font-size: 29px;
    color: var(--grey-text); margin-top: -6px;
  }

  .contact {
    position: absolute; left: 510px; top: 440px; display: flex; align-items: center;
    font-family: 'Lato', sans-serif; font-weight: 700; font-size: 22px; color: var(--white);
  }
  .contact__item { display: flex; align-items: center; gap: 8px; margin-right: 18px; }
  .contact__square { width: 20px; height: 20px; background: var(--white); border-radius: 3px; }
  .contact__phone-icon {
    width: 22px; height: 22px; background: var(--yellow); border-radius: 4px;
    display: flex; align-items: center; justify-content: center;
  }
</style>
</head>
<body>
  <div class="flyer">
    <div class="flyer__photo" role="img" aria-label="Photo of a smiling mother holding a book walking her daughter to school"></div>

    <svg class="flyer__shapes" viewBox="0 0 1100 530" width="1100" height="530" aria-hidden="true">
      <path fill="var(--purple)" d="M0 0 H1100 V150 C1000 162,860 210,700 196 C560 182,420 88,280 98 C160 108,60 175,0 192 Z"/>
      <path fill="var(--pink)" d="M0 0 H1100 V122 C1000 135,860 185,700 170 C560 155,420 62,280 72 C160 82,60 150,0 168 Z"/>
      <path fill="var(--pink)" d="M0 396 C120 426,220 456,340 451 C480 441,560 366,700 371 C850 376,980 426,1100 456 V530 H0 Z"/>
      <path fill="var(--white)" d="M0 403 C120 433,220 463,340 458 C480 448,560 373,700 378 C850 383,980 433,1100 463 V530 H0 Z"/>
      <path fill="var(--purple)" d="M0 410 C120 440,220 470,340 465 C480 455,560 380,700 385 C850 390,980 440,1100 470 V530 H0 Z"/>
    </svg>

    <div class="flyer__produce" role="img" aria-label="Photo of real food and fitness items: a fresh apple, a water bottle, green dumbbells, a tape measure and a rolled towel"></div>

    <div class="offer">
      <p class="offer__headline">MOBILE WEIGHT LOSS CONSULTANT- OFFERING AT YOUR HOME OR WORK CONSULTS.</p>
      <p class="offer__experience">10 YEARS EXPERIENCE AS A WEIGHT LOSS CONSULTANT</p>
      <p class="offer__terms">NO CONTRACTS. YOU HAVE NOTHING TO LOSE APART FROM<br>WHAT YOU WANT TO LOSE</p>
    </div>

    <div class="brand-badge">
      <span class="brand-badge__name">Brightpath<br>Wellness Guide</span>
    </div>

    <div class="message">
      <p><span class="message__headline">Wow, Spring Is Near!</span><span class="message__question">Kids back at school?</span></p>
      <p class="message__sub">Mine too Time to look after yourself,your worth it.</p>
    </div>

    <div class="contact">
      <div class="contact__item">
        <span class="contact__square"></span>
        <span>BrightpathWellnessGuide</span>
      </div>
      <div class="contact__item">
        <span class="contact__phone-icon">
          <svg width="14" height="14" viewBox="0 0 24 24" aria-hidden="true">
            <path fill="var(--purple)" d="M6.6 10.8a15 15 0 0 0 6.6 6.6l2.2-2.2c.3-.3.7-.4 1-.2 1.1.4 2.3.6 3.6.6.6 0 1 .4 1 1V20c0 .6-.4 1-1 1C10.6 21 3 13.4 3 4c0-.6.4-1 1-1h3.5c.6 0 1 .4 1 1 0 1.3.2 2.5.6 3.6.1.3 0 .7-.2 1z"/>
          </svg>
        </span>
        <span>0439 582 706</span>
      </div>
    </div>
  </div>
</body>
</html>
```